Social Media Marketing website

Need website designed for social media marketing company BrightLoop.com
Do no currently have logo.
Pages:
Main
Services
Order
Contact
Please use dummy text for now. I will provide content to winner later to add.
Main page should clearly show the steps with some sort of graphic: Establish, Engage, Analyze.
Services provided (steps):
1) Establish social media presence
2) Social media management and advertising
3) Analyze and engage
Site should be simple, clean and attractive. Design examples:
http://plinkster.com/
http://www.quillbase.com/
http://www.harrowvalemq.com/
Be creative! It should not look like a template.
Updates
Updated examples.
Contact me for questions.
dave@brightloop.com
3) Analyze and engage
Advertising

```html
<!DOCTYPE html>
<html lang="en">
<head>
<meta charset="utf-8">
<title>BrightLoop – Social Media Marketing</title>
<link rel="stylesheet" href="https://fonts.googleapis.com/css2?family=Arimo:wght@400;700&family=Cuprum:ital,wght@0,700;1,400&display=swap">
<style>
:root{
  --bar-dark:#3c3f48;
  --header-top:#ffffff;
  --header-bottom:#d9d9d9;
  --band-top:#5d6870;
  --band-bottom:#2c353a;
  --band-line:#20282c;
  --heading:#4a5560;
  --text:#3a3a3a;
  --muted:#666a70;
  --rule:#c9cdd1;
  --card-top:#ffffff;
  --card-bottom:#d8d8d8;
  --button-top:#5a646b;
  --button-bottom:#252d31;
  --link-blue:#2a88b8;
  --footer:#232b2f;
  --footer-text:#8a9094;
  --green:#7ccc2c;
  --blue:#3f9ccc;
  --red:#c62a2a;
}
*{margin:0;padding:0;box-sizing:border-box}
html,body{width:1200px;height:939px;overflow:hidden}
body{position:relative;font-family:"Arimo",Arial,sans-serif;color:var(--text);background:#fff}
.top-bar{position:absolute;left:0;top:0;width:1200px;height:9px;background:linear-gradient(#6a6d76,var(--bar-dark))}
.header{position:absolute;left:0;top:9px;width:1200px;height:340px;background:linear-gradient(var(--header-top),#ececec 40%,var(--header-bottom))}
.brand{position:absolute;left:285px;top:18px;display:flex;align-items:center;gap:10px;font-family:"Cuprum",sans-serif;font-weight:700;font-size:40px;color:#2f3437;line-height:1}
.brand-mark{width:26px;height:26px;background:#c9cbcd;border-radius:3px}
.main-nav{position:absolute;left:621px;top:29px;display:flex;gap:16px;list-style:none}
.main-nav a{display:block;width:64px;height:19px;border-radius:4px;background:linear-gradient(#f0f0f0,#d6d6d6);font-size:11px;color:#333;text-align:center;line-height:19px;text-decoration:none;letter-spacing:.3px}
.benefits{position:absolute;left:420px;top:94px;width:513px;height:210px;border-radius:14px;background:linear-gradient(#fdfdfd,#dcdcdc);box-shadow:2px 4px 6px rgba(0,0,0,.3)}
.benefits h1{position:absolute;left:136px;top:8px;width:345px;padding-bottom:6px;border-bottom:1px solid var(--rule);font-family:"Cuprum",sans-serif;font-style:italic;font-weight:400;font-size:22px;color:var(--heading)}
.benefits ul{position:absolute;left:144px;top:47px;width:345px;list-style:none;font-size:13px;line-height:17px}
.benefits li{margin-bottom:3px}
.steps-chart{position:absolute;left:300px;top:75px;width:244px;height:250px}
.feature-band{position:absolute;left:0;top:349px;width:1200px;height:57px;background:linear-gradient(var(--band-top),var(--band-bottom));border-top:1px solid #7c868c}
.features{position:absolute;left:260px;top:0;display:flex;height:57px;list-style:none}
.feature{position:relative;height:57px;border-left:1px solid var(--band-line);box-shadow:inset 1px 0 0 #6e787e}
.feature:last-child{border-right:1px solid var(--band-line)}
.feature-word{position:absolute;top:3px;font-family:"Cuprum",sans-serif;font-style:italic;font-size:21px;color:#d2d6d9}
.feature-sub{position:absolute;top:27px;font-size:15px;color:#15191b;white-space:nowrap}
.feature-icon{position:absolute;top:5px;width:46px;height:46px;border-radius:6px}
.content{position:absolute;left:0;top:406px;width:1200px;height:492px;background:linear-gradient(#ffffff,#e3e3e3)}
.package{position:absolute;top:46px;height:201px;border-radius:10px;background:linear-gradient(var(--card-top),var(--card-bottom));box-shadow:1px 4px 5px rgba(0,0,0,.3)}
.package h2{position:absolute;left:52px;top:10px;right:14px;padding-bottom:3px;border-bottom:1px solid var(--rule);font-family:"Cuprum",sans-serif;font-style:italic;font-weight:400;font-size:22px;color:var(--heading)}
.coin{position:absolute;left:12px;top:6px;width:34px;height:34px;border-radius:50%}
.coin-bronze{background:radial-gradient(circle at 40% 40%,#e4a47a,#a2542c)}
.coin-silver{background:radial-gradient(circle at 40% 40%,#d8d8d8,#6d6d6d)}
.coin-gold{background:radial-gradient(circle at 40% 40%,#f2e27a,#b39a20)}
.package ul{position:absolute;left:38px;top:55px;list-style:none;font-size:13px;line-height:20px}
.purchase{position:absolute;left:47px;top:157px;width:133px;height:33px;border:1px solid #1d2326;border-radius:4px;background:linear-gradient(var(--button-top),var(--button-bottom));box-shadow:inset 0 1px 0 #7a858c;color:#fff;font-weight:700;font-size:15px;text-align:center;line-height:31px;text-decoration:none}
.mobile{position:absolute;left:225px;top:285px;width:562px;height:168px;border:1px solid #c6c6c6;border-radius:4px;background:linear-gradient(#f4f4f4,#ececec)}
.mobile-art{position:absolute;left:14px;top:8px;width:136px;height:152px;border-radius:10px;background:linear-gradient(135deg,#e6e6e6,#9aa2ac 55%,#3e4a5a)}
.mobile h2{position:absolute;left:158px;top:12px;font-family:"Cuprum",sans-serif;font-style:italic;font-weight:400;font-size:22px;color:var(--heading)}
.mobile p{position:absolute;left:160px;top:42px;width:380px;font-size:13px;line-height:15.5px;color:var(--muted)}
.testimonials{position:absolute;left:806px;top:296px;width:230px}
.testimonials h2{font-family:"Cuprum",sans-serif;font-style:italic;font-weight:400;font-size:22px;color:var(--heading);margin-bottom:4px}
.testimonials blockquote{font-size:13px;line-height:15px;color:var(--muted)}
.testimonials cite{display:block;margin:4px 0 22px;font-size:11px;font-weight:700;font-style:italic;color:var(--link-blue)}
.footer{position:absolute;left:0;top:898px;width:1200px;height:41px;background:var(--footer);color:var(--footer-text);font-size:11px;text-align:center;line-height:34px}
</style>
</head>
<body>
<div class="top-bar"></div>

<header class="header">
  <div class="brand"><span>BrightLoop</span><span class="brand-mark"></span></div>
  <ul class="main-nav">
    <li><a href="#">home</a></li>
    <li><a href="#">examples</a></li>
    <li><a href="#">order</a></li>
    <li><a href="#">contact</a></li>
  </ul>

  <section class="benefits">
    <h1>Benefits of Having A Trendy FanPage</h1>
    <ul>
      <li>-Alert your fans of&nbsp; offers, events and discounts instantly</li>
      <li>- Easily create new product or service campaigns online</li>
      <li>- With half a billion users on Circlebook, you can drive lots<br>&nbsp;&nbsp;&nbsp;of traffic to your website through your fan page</li>
      <li>- You can have unlimited Circlebook users who like you - they are all potential clients!</li>
      <li>- Anyone can access your fan page, they can find you on Circlebook or from a search on Searchly</li>
    </ul>
  </section>

  <svg class="steps-chart" viewBox="300 75 244 250" aria-label="Steps: Establish, Engage, Analyze">
    <defs>
      <linearGradient id="g-green" x1="0" y1="0" x2="0" y2="1"><stop offset="0" stop-color="#6cbf2a"/><stop offset="1" stop-color="#8fdc2e"/></linearGradient>
      <linearGradient id="g-blue" x1="0" y1="0" x2="0" y2="1"><stop offset="0" stop-color="#2f86b8"/><stop offset="1" stop-color="#5ab2dc"/></linearGradient>
      <linearGradient id="g-red" x1="0" y1="0" x2="0" y2="1"><stop offset="0" stop-color="#d83434"/><stop offset="1" stop-color="#a81e1e"/></linearGradient>
      <radialGradient id="g-shadow"><stop offset="0" stop-color="#000" stop-opacity=".35"/><stop offset="1" stop-color="#000" stop-opacity="0"/></radialGradient>
    </defs>
    <ellipse cx="425" cy="315" rx="125" ry="9" fill="url(#g-shadow)"/>
    <path d="M421 197 L421 79 A118 118 0 0 0 319 256 Z" fill="url(#g-green)"/>
    <path d="M421 197 L421 79 A118 118 0 0 1 523 256 Z" fill="url(#g-blue)"/>
    <path d="M421 197 L523 256 A118 118 0 0 1 319 256 Z" fill="url(#g-red)"/>
    <path d="M421 82 A115 115 0 0 0 306 197" fill="none" stroke="#b5ec7a" stroke-width="3" opacity=".7"/>
    <path d="M421 82 A115 115 0 0 1 536 197" fill="none" stroke="#9ad4f2" stroke-width="3" opacity=".7"/>
    <g font-family="Cuprum, sans-serif" font-weight="700" font-size="17" fill="#fff" text-anchor="middle">
      <text x="368" y="180">Establish</text>
      <text x="471" y="180">Engage</text>
      <text x="422" y="261">Analyze</text>
    </g>
  </svg>
</header>

<nav class="feature-band">
  <ul class="features">
    <li class="feature" style="width:190px"><span class="feature-word" style="left:25px">improved</span><span class="feature-sub" style="left:15px">communication</span><span class="feature-icon" role="img" aria-label="Mailbox icon" style="left:135px;background:linear-gradient(#9fd0ee,#3a7fb0)"></span></li>
    <li class="feature" style="width:160px"><span class="feature-word" style="left:25px">creative</span><span class="feature-sub" style="left:14px">design/look</span><span class="feature-icon" role="img" aria-label="Design tools icon" style="left:100px;background:linear-gradient(#e6e6e6,#8fb070)"></span></li>
    <li class="feature" style="width:170px"><span class="feature-word" style="left:25px">attract</span><span class="feature-sub" style="left:15px">larger fanbase</span><span class="feature-icon" role="img" aria-label="User info icon" style="left:118px;background:linear-gradient(#c89a70,#2d6fb0)"></span></li>
    <li class="feature" style="width:170px"><span class="feature-word" style="left:25px">smarter</span><span class="feature-sub" style="left:15px">for business</span><span class="feature-icon" role="img" aria-label="Puzzle pieces icon" style="left:110px;background:linear-gradient(135deg,#f0c020,#3a70c0 50%,#c03030)"></span></li>
  </ul>
</nav>

<main class="content">
  <section class="package" style="left:228px;width:227px">
    <span class="coin coin-bronze" role="img" aria-label="Bronze coins icon"></span>
    <h2>Standard Package</h2>
    <ul><li>- Custom Welcome Page</li><li>- Custom Profile Banner</li><li>- No Opt-In Form</li><li>- No Video</li></ul>
    <a class="purchase" href="#">Purchase</a>
  </section>
  <section class="package" style="left:498px;width:225px">
    <span class="coin coin-silver" role="img" aria-label="Silver coins icon"></span>
    <h2>Advance Package</h2>
    <ul><li>- Custom Welcome Page</li><li>- Custom Profile Banner</li><li>- Opt-In Form</li><li>- Video</li></ul>
    <a class="purchase" href="#">Purchase</a>
  </section>
  <section class="package" style="left:768px;width:223px">
    <span class="coin coin-gold" role="img" aria-label="Gold coins icon"></span>
    <h2>Ultimate Package</h2>
    <ul><li>- Custom Welcome Page</li><li>- Custom Banner</li><li>- Opt-In Form</li><li>- Searchly Analytics Setup</li><li>- Video</li></ul>
    <a class="purchase" href="#">Purchase</a>
  </section>

  <section class="mobile">
    <div class="mobile-art" role="img" aria-label="Smartphone and desktop showing a fan page"></div>
    <h2>Manage your fanpage from your smartphone!</h2>
    <p>- Lorem ipsum dolor sit amet, consectetuer adipiscing elit, sed diam nonummy nibh euismod tincidunt ut laoreet dolore magna aliquam erat volutpat. Ut wisi enim ad minim veniam, quis nostrud exerci tation ullamcorper suscipit lobortis nisl ut aliquip ex ea commodo consequat. Duis autem vel eum iriure dolor in hendrerit in vulputate velit esse molestie consequat.</p>
  </section>

  <aside class="testimonials">
    <h2>Testimonials</h2>
    <blockquote>"Great design! I can't believe how much this improved my fanbase! I saw instant results."</blockquote>
    <cite>-Sam Porter</cite>
    <blockquote>"Great design! I can't believe how much this improved my fanbase! I saw instant results."</blockquote>
    <cite>-Sam Porter</cite>
  </aside>
</main>

<footer class="footer">© 2011 Brightloop.com</footer>
</body>
</html>
```